New Company Business Card design

Looking for a corporate looking business card utilising my new logo design - the logo i would like embossed as one option and flat as another - simplistic but stylish - less is more - we are an import export business launching into the market - i would like a couple of options as main background - Grey or Black

```html
<!DOCTYPE html>
<html lang="en">
<head>
<meta charset="utf-8">
<title>Meridian Trade Partners – Business Card</title>
<link rel="stylesheet" href="https://fonts.googleapis.com/css2?family=Cinzel:wght@500;600&family=Roboto:wght@400&display=swap">
<style>
  :root {
    --card-charcoal: #2a2b2d;
    --card-grey: #4a4c4f;
    --accent-grey: #8c8e91;
    --ink-dark: #2a2b2d;
    --paper: #ffffff;
    --backdrop: #e6e7e9;
    --card-radius: 19px;
  }
  * { margin: 0; padding: 0; box-sizing: border-box; }
  html, body { width: 1200px; height: 849px; overflow: hidden; }
  body { background: var(--backdrop); position: relative; font-family: "Roboto", Arial, sans-serif; }

  .card {
    position: absolute;
    left: 262px;
    width: 652px;
    height: 355px;
    border-radius: var(--card-radius);
    overflow: hidden;
    box-shadow: 0 6px 16px rgba(0,0,0,0.18);
  }
  .card--front { top: 46px; background: var(--card-grey); }
  .card--back { top: 446px; background: var(--card-charcoal); }

  .brand-name {
    font-family: "Cinzel", Georgia, serif;
    font-weight: 600;
    text-transform: uppercase;
    text-align: center;
    line-height: 1.15;
  }
  .card--front .brand-name {
    position: absolute;
    left: 0; right: 0; top: 50%;
    transform: translateY(-50%);
    color: var(--paper);
    font-size: 32px;
    letter-spacing: 3px;
  }

  .back-art { position: absolute; inset: 0; }
  .card--back .brand-name {
    position: absolute;
    left: 36px; top: 178px;
    width: 250px;
    transform: translateY(-50%);
    color: var(--ink-dark);
    font-size: 21px;
    letter-spacing: 1.5px;
  }

  .holder {
    position: absolute;
    right: 45px; top: 36px;
    text-align: right;
    color: var(--paper);
  }
  .holder__name {
    font-family: "Cinzel", Georgia, serif;
    font-weight: 600;
    font-size: 29px;
    letter-spacing: 1.5px;
    line-height: 1.1;
  }
  .holder__role { font-size: 15px; margin-top: 3px; }

  .address {
    position: absolute;
    right: 45px; top: 196px;
    text-align: right;
    color: var(--paper);
    font-size: 15px;
    line-height: 20px;
    font-style: normal;
  }

  .contacts {
    position: absolute;
    right: 45px; top: 261px;
    list-style: none;
    color: var(--paper);
    font-size: 15px;
    line-height: 20px;
  }
  .contacts__item { display: flex; justify-content: flex-end; align-items: center; gap: 8px; }
  .contacts__icon { width: 12px; height: 12px; fill: var(--paper); flex: none; }
</style>
</head>
<body>

  <section class="card card--front" aria-label="Card front">
    <div class="brand-name">Meridian Trade Partners</div>
  </section>

  <section class="card card--back" aria-label="Card back">
    <svg class="back-art" width="652" height="355" viewBox="0 0 652 355" aria-hidden="true">
      <circle cx="152" cy="178" r="182" fill="var(--accent-grey)"/>
      <circle cx="137" cy="178" r="182" fill="var(--paper)"/>
    </svg>

    <div class="brand-name">Meridian Trade Partners</div>

    <div class="holder">
      <div class="holder__name">DANIEL REYES</div>
      <div class="holder__role">Founder &amp; CEO</div>
    </div>

    <address class="address">
      Suite 210, P.O Box #48120<br>
      Harbor, Your country
    </address>

    <ul class="contacts">
      <li class="contacts__item">(000) 000 0000
        <svg class="contacts__icon" viewBox="0 0 24 24"><path d="M6.6 10.8a15.1 15.1 0 0 0 6.6 6.6l2.2-2.2a1 1 0 0 1 1-.25 11.4 11.4 0 0 0 3.6.57 1 1 0 0 1 1 1V20a1 1 0 0 1-1 1A17 17 0 0 1 3 4a1 1 0 0 1 1-1h3.5a1 1 0 0 1 1 1c0 1.25.2 2.45.57 3.57a1 1 0 0 1-.25 1z"/></svg>
      </li>
      <li class="contacts__item">info@meridiantrade.com
        <svg class="contacts__icon" viewBox="0 0 24 24"><path d="M2 5h20v2l-10 6L2 7z"/><path d="M2 9.3l10 6 10-6V19H2z"/></svg>
      </li>
      <li class="contacts__item">www.meridiantrade.com
        <svg class="contacts__icon" viewBox="0 0 24 24"><circle cx="12" cy="12" r="10"/><path d="M2 12h20M12 2c3 3 3 17 0 20M12 2c-3 3-3 17 0 20" stroke="var(--card-charcoal)" stroke-width="1.6" fill="none"/></svg>
      </li>
    </ul>
  </section>

</body>
</html>
```